A Weather Forecasting Site needs designs

We need a website design for our new venture which is a weather forecasting website. This website should have the latest design trends.

Menu
Weather, Maps, Videos and Photos

The home page requirements are as follows:
- Search Bar
- Local Weather
- Weather forecast of major cities in the World
Favorite locations
- Space for ADs
- Email signup

Weather Details page
This page will be redirected from the home page when you click on any of the weather forecast section

We are open to all kinds of designs and ideas. Feel free to you colors which suite your design.

```html
<!DOCTYPE html>
<html lang="en">
<head>
<meta charset="utf-8">
<title>Skyvane Weather</title>
<link href="https://fonts.googleapis.com/css2?family=Josefin+Sans:wght@300;400;600;700&family=Montserrat:wght@400;600;700&display=swap" rel="stylesheet">
<style>
:root{
  --ink:#2b2b2b;
  --muted:#8a8a8a;
  --white:#ffffff;
  --accent-blue:#3a93d6;
  --nav-pill:#cfe6f8;
  --gold:#e0b22c;
  --green:#2fae5f;
  --go-green:#2ec46a;
  --city-red:#d23b3b;
  --card-border:#e6e6e6;
  --pill-bg:rgba(70,60,50,.55);
  --footer-grey:#9b9b9b;
}
*{box-sizing:border-box;margin:0;padding:0}
html,body{width:1200px;height:2356px;overflow:hidden;background:var(--white)}
body{position:relative;font-family:"Josefin Sans",sans-serif;color:var(--ink)}
.abs{position:absolute}

/* nav */
.brand{left:82px;top:10px;display:flex;align-items:center;gap:10px;font-family:"Montserrat",sans-serif;font-weight:700;font-size:17px;letter-spacing:6px;color:#111}
.brand .dot{width:26px;height:26px;border:2px solid #111;border-radius:50%}
.nav-item{top:3px;height:44px;display:flex;align-items:center;gap:18px;font-size:12px;color:#4a6b8a;font-family:"Montserrat",sans-serif}
.nav-item svg{width:20px;height:20px}
.nav-item.active{left:514px;width:130px;padding-left:14px;background:var(--nav-pill);border-radius:22px;color:var(--accent-blue);box-shadow:0 2px 6px rgba(58,147,214,.25)}
.nav-item.active .sep{width:2px;height:22px;background:var(--accent-blue)}

/* hero */
.hero{left:0;top:52px;width:1200px;height:509px;border-radius:14px 14px 0 0;overflow:hidden;
  background:linear-gradient(180deg,#a7a59a 0%,#8e8a78 30%,#6f7562 55%,#5d6a64 75%,#6f6a5e 100%)}
.search{left:866px;top:64px;width:334px;height:30px;border-bottom:2px solid rgba(255,255,255,.85);color:rgba(255,255,255,.9);font-size:11px;padding:4px 0 0 0}
.search svg{position:absolute;right:8px;top:2px;width:16px;height:16px}
.eyebrow{left:83px;top:172px;font-family:"Montserrat",sans-serif;font-size:11px;letter-spacing:2px;color:var(--gold);font-weight:600}
.city{left:83px;top:194px;font-size:42px;font-weight:600;color:var(--white)}
.country{left:83px;top:240px;font-size:34px;font-weight:300;color:rgba(255,255,255,.85)}
.change-loc{left:889px;top:363px;width:311px;height:56px;background:var(--accent-blue);border-radius:28px 0 0 28px;display:flex;align-items:center;padding-left:26px;gap:28px;color:var(--white);font-size:15px;letter-spacing:.5px}
.change-loc svg{width:22px;height:28px}
.tab{top:524px;display:flex;align-items:center;gap:18px;font-family:"Montserrat",sans-serif;font-size:11px;letter-spacing:2px;color:var(--white);font-weight:600}
.tab.dim{color:rgba(255,255,255,.6);font-weight:400}
.tab svg{width:20px;height:20px}
.bar-gold{left:0;top:556px;width:377px;height:5px;background:var(--gold)}
.bar-green{left:377px;top:556px;width:388px;height:5px;background:var(--green)}

/* current weather strip */
.strip{left:0;top:561px;width:1200px;height:248px;background:linear-gradient(100deg,#6f7f86 0%,#8a8375 25%,#a08e78 55%,#8f7f6c 80%,#9a8a78 100%)}
.temp-now{left:90px;top:588px;font-size:132px;font-weight:600;color:var(--white);line-height:1}
.temp-now sup{font-size:60px;position:relative;top:-64px;margin-left:6px}
.today{left:74px;top:727px;font-family:"Montserrat",sans-serif;font-size:10px;letter-spacing:1px;color:var(--gold)}
.date-pill{left:74px;top:748px;width:162px;height:31px;border-radius:8px;background:rgba(60,60,60,.55);color:var(--white);font-size:17px;display:flex;align-items:center;justify-content:center}
.date-pill sup{font-size:10px}
.vdiv{left:270px;top:594px;width:1px;height:120px;background:rgba(255,255,255,.45)}
.big-sun{left:303px;top:594px;width:132px;height:132px}
.wind{left:303px;top:755px;font-size:17px;color:var(--white);word-spacing:6px}
.days{left:503px;top:561px;width:697px;height:248px;display:flex}
.day{flex:1;border-left:1px solid rgba(255,255,255,.25);display:flex;flex-direction:column;align-items:center;padding-top:28px;color:var(--white)}
.day .pill{width:86px;height:19px;border-radius:9px;background:var(--pill-bg);font-size:10px;display:flex;align-items:center;justify-content:center}
.day svg{width:60px;height:60px;margin-top:34px}
.day .t{font-size:20px;margin-top:18px}

/* cities */
.section-title{left:83px;top:850px;font-family:"Montserrat",sans-serif;font-size:11px;letter-spacing:2px;font-weight:600;color:#444}
.card{width:269px;height:355px;border:2px solid var(--card-border);border-radius:12px;overflow:hidden;background:var(--white);box-shadow:0 3px 8px rgba(0,0,0,.06);text-align:center}
.card .photo{height:204px}
.card .name{margin-top:38px;font-family:"Montserrat",sans-serif;font-size:11px;letter-spacing:2px;color:var(--city-red);font-weight:600}
.card .when{margin-top:8px;font-size:11px;letter-spacing:3px;color:var(--muted)}
.card .when sup{font-size:7px}
.card .deg{margin-top:18px;font-size:32px;letter-spacing:6px;color:#222}
.card .deg sup{font-size:18px}
.more{left:573px;top:1722px;width:54px;height:54px;border-radius:50%;background:#dcdcdc;color:var(--white);font-size:18px;letter-spacing:3px;display:flex;align-items:center;justify-content:center}

/* newsletter */
.newsletter{left:0;top:1846px;width:1200px;height:199px;background:linear-gradient(180deg,#8aa4bc 0%,#6f8ca8 45%,#5f7f9e 70%,#7d98b2 100%)}
.nl-title{left:0;top:1886px;width:1200px;text-align:center;font-family:"Montserrat",sans-serif;font-size:19px;letter-spacing:4px;color:var(--white);font-weight:600}
.nl-sub{left:0;top:1916px;width:1200px;text-align:center;font-size:13px;color:rgba(255,255,255,.9)}
.nl-input{left:369px;top:1950px;width:356px;height:42px;background:var(--white);border-radius:21px 0 0 21px;color:#b5b5b5;font-size:13px;padding:15px 0 0 34px}
.nl-go{left:712px;top:1950px;width:121px;height:42px;background:var(--go-green);border-radius:0 21px 21px 0;color:var(--white);font-size:19px;letter-spacing:4px;display:flex;align-items:center;justify-content:center;font-weight:600}

/* footer */
.foot-brand{left:0;top:2118px;width:1200px;display:flex;justify-content:center;align-items:center;gap:14px;font-family:"Montserrat",sans-serif;font-weight:700;font-size:27px;letter-spacing:10px;color:#111}
.foot-brand .dot{width:40px;height:40px;border:3px solid #111;border-radius:50%}
.copy{left:0;top:2197px;width:1200px;text-align:center;font-size:11px;color:var(--footer-grey)}
.links{left:0;top:2218px;width:1200px;text-align:center;font-size:12px;color:#777;word-spacing:3px}
.social{left:0;top:2258px;width:1200px;display:flex;justify-content:center;gap:32px}
.social span{width:30px;height:30px;border-radius:50%;background:#d0d0d0}
</style>
</head>
<body>

<!-- header -->
<div class="abs brand"><span class="dot"></span>Skyvane</div>
<div class="abs nav-item active">
  <svg viewBox="0 0 20 20" fill="none" stroke="currentColor" stroke-width="1.4"><circle cx="10" cy="10" r="4"/><path d="M10 1v3M10 16v3M1 10h3M16 10h3M3.6 3.6l2.1 2.1M14.3 14.3l2.1 2.1M3.6 16.4l2.1-2.1M14.3 5.7l2.1-2.1"/></svg>
  <span class="sep"></span>Weather
</div>
<div class="abs nav-item" style="left:696px">
  <svg viewBox="0 0 20 20" fill="none" stroke="#3a93d6" stroke-width="1.4"><circle cx="10" cy="10" r="8"/><circle cx="10" cy="10" r="2.5"/></svg>Maps
</div>
<div class="abs nav-item" style="left:845px">
  <svg viewBox="0 0 20 20" fill="none" stroke="#3a93d6" stroke-width="1.4"><circle cx="6" cy="6" r="3"/><circle cx="13" cy="6" r="3"/><rect x="2" y="10" width="12" height="7" rx="1"/><path d="M14 12l4-2v7l-4-2"/></svg>Videos
</div>
<div class="abs nav-item" style="left:999px">
  <svg viewBox="0 0 20 20" fill="none" stroke="#3a93d6" stroke-width="1.4"><rect x="2" y="5" width="16" height="12" rx="2"/><circle cx="10" cy="11" r="3.2"/><path d="M7 5l1.5-2h3L13 5"/></svg>Photos
</div>

<!-- hero -->
<div class="abs hero" role="img" aria-label="Aerial photo of a mountain peak rising over a green bay with a city along the shore"></div>
<div class="abs search">Search for a Loction, Place , Photo etc...
  <svg viewBox="0 0 16 16" fill="none" stroke="#fff" stroke-width="1.5"><circle cx="6.5" cy="6.5" r="5"/><path d="M10.5 10.5l4 4"/></svg>
</div>
<div class="abs eyebrow">LOCAL WEATHER</div>
<div class="abs city">Rio De Janeiro</div>
<div class="abs country">Brazil</div>
<div class="abs change-loc">
  <svg viewBox="0 0 22 28" fill="none" stroke="#fff" stroke-width="1.6"><path d="M11 26S2 15 2 10a9 9 0 0118 0c0 5-9 16-9 16z"/><circle cx="11" cy="10" r="3.2"/></svg>
  Change Location
</div>
<div class="abs tab" style="left:110px">
  <svg viewBox="0 0 20 20" fill="none" stroke="#fff" stroke-width="1.3"><circle cx="10" cy="10" r="4"/><path d="M10 1v3M10 16v3M1 10h3M16 10h3M3.6 3.6l2.1 2.1M14.3 14.3l2.1 2.1M3.6 16.4l2.1-2.1M14.3 5.7l2.1-2.1"/></svg>WEATHER
</div>
<div class="abs tab dim" style="left:462px">
  <svg viewBox="0 0 20 20" fill="none" stroke="rgba(255,255,255,.6)" stroke-width="1.3"><path d="M10 2l2.4 5 5.4.6-4 3.7 1.1 5.3L10 14l-4.9 2.6 1.1-5.3-4-3.7 5.4-.6z"/></svg>FAVORITE LOCATIONS
</div>
<div class="abs bar-gold"></div>
<div class="abs bar-green"></div>

<!-- current weather -->
<div class="abs strip"></div>
<div class="abs temp-now">31<sup>°</sup></div>
<div class="abs today">TODAY</div>
<div class="abs date-pill">Monday 26<sup>th</sup></div>
<div class="abs vdiv"></div>
<svg class="abs big-sun" viewBox="0 0 132 132" fill="none" stroke="#fff" stroke-width="6" stroke-linecap="round"><circle cx="66" cy="66" r="28"/><path d="M66 4v18M66 110v18M4 66h18M110 66h18M22 22l13 13M97 97l13 13M22 110l13-13M97 35l13-13"/></svg>
<div class="abs wind">2mph / 32°</div>

<div class="abs days">
  <div class="day"><div class="pill">Tuesday</div>
    <svg viewBox="0 0 60 60" fill="none" stroke="#fff" stroke-width="2" stroke-linecap="round"><circle cx="34" cy="22" r="8"/><path d="M34 6v5M48 22h5M44 12l3-3M24 12l-3-3M44 32l3 3"/><path d="M14 46h26a8 8 0 000-16 11 11 0 00-21 2 7 7 0 00-5 14z" fill="rgba(255,255,255,.15)"/></svg>
    <div class="t">25°</div></div>
  <div class="day"><div class="pill">Wednesday</div>
    <svg viewBox="0 0 60 60" fill="none" stroke="#fff" stroke-width="2"><path d="M14 42h32a8 8 0 000-16 13 13 0 00-25 2 7 7 0 00-7 14z"/></svg>
    <div class="t">15°</div></div>
  <div class="day"><div class="pill">Thursday</div>
    <svg viewBox="0 0 60 60" fill="none" stroke="#fff" stroke-width="2" stroke-linecap="round"><path d="M14 34h30a8 8 0 000-16 12 12 0 00-23 2 7 7 0 00-7 14z"/><path d="M18 40l-3 6M26 40l-3 6M34 40l-3 6M40 38h12M42 43h14M44 48h8"/></svg>
    <div class="t">14°</div></div>
  <div class="day"><div class="pill">Friday</div>
    <svg viewBox="0 0 60 60" fill="none" stroke="#fff" stroke-width="2" stroke-linecap="round"><path d="M14 34h32a8 8 0 000-16 12 12 0 00-23 2 7 7 0 00-9 14z"/><path d="M22 38v8M18 42h8M34 38v8M30 42h8M28 48v6M25 51h6"/></svg>
    <div class="t">8°</div></div>
  <div class="day"><div class="pill">Saturday</div>
    <svg viewBox="0 0 60 60" fill="none" stroke="#fff" stroke-width="2" stroke-linecap="round" stroke-linejoin="round"><path d="M14 34h32a8 8 0 000-16 12 12 0 00-23 2 7 7 0 00-9 14z"/><path d="M20 38l-3 6M40 38l-3 6M30 36l-4 8h6l-4 8"/></svg>
    <div class="t">19°</div></div>
  <div class="day"><div class="pill">Sunday</div>
    <svg viewBox="0 0 60 60" fill="none" stroke="#fff" stroke-width="2" stroke-linecap="round"><circle cx="36" cy="18" r="7"/><path d="M36 4v4M50 18h4M46 8l3-3M26 8l-3-3"/><path d="M12 38h28a8 8 0 000-16 11 11 0 00-21 2 7 7 0 00-7 14z"/><path d="M18 44l-2 5M26 44l-2 5M34 44l-2 5"/></svg>
    <div class="t">20°</div></div>
</div>

<!-- major cities -->
<div class="abs section-title">WEATHER FORECAST OF MAJOR CITIES IN THE WORLD</div>

<div class="abs card" style="left:143px;top:916px">
  <div class="photo" role="img" aria-label="Red shrine gate standing in a calm lake" style="background:linear-gradient(180deg,#6d6a6a,#9a8a84 50%,#7a6e6a)"></div>
  <div class="name">HAKONE-MACHI</div><div class="when">MONDAY | 26<sup>TH</sup> | 23:21</div><div class="deg">29<sup>O</sup></div>
</div>
<div class="abs card" style="left:465px;top:916px">
  <div class="photo" role="img" aria-label="Iron lattice tower above a river and trees under a cloudy sky" style="background:linear-gradient(180deg,#d6d8da,#c4c7c6 60%,#7f8d74)"></div>
  <div class="name">HAKONE-MACHI</div><div class="when">MONDAY | 26<sup>TH</sup> | 23:21</div><div class="deg">29<sup>O</sup></div>
</div>
<div class="abs card" style="left:789px;top:916px">
  <div class="photo" role="img" aria-label="Suspension bridge lit at night over dark water" style="background:linear-gradient(180deg,#3a3d45,#4c4a4a 55%,#2a2c33)"></div>
  <div class="name">HAKONE-MACHI</div><div class="when">MONDAY | 26<sup>TH</sup> | 23:21</div><div class="deg">29<sup>O</sup></div>
</div>
<div class="abs card" style="left:143px;top:1318px">
  <div class="photo" role="img" aria-label="Gothic clock tower against a pale sky" style="background:linear-gradient(180deg,#c9d6d8,#b7c1bd 55%,#8c7a58)"></div>
  <div class="name">HAKONE-MACHI</div><div class="when">MONDAY | 26<sup>TH</sup> | 23:21</div><div class="deg">29<sup>O</sup></div>
</div>
<div class="abs card" style="left:465px;top:1318px">
  <div class="photo" role="img" aria-label="Arched walls of an ancient stone amphitheatre" style="background:linear-gradient(180deg,#5f5f5e,#7c7873 50%,#55524e)"></div>
  <div class="name">HAKONE-MACHI</div><div class="when">MONDAY | 26<sup>TH</sup> | 23:21</div><div class="deg">29<sup>O</sup></div>
</div>
<div class="abs card" style="left:789px;top:1318px">
  <div class="photo" role="img" aria-label="City bridge and towers with red lights reflected in water at night" style="background:linear-gradient(180deg,#27303f,#3a3344 55%,#5a2a30)"></div>
  <div class="name">HAKONE-MACHI</div><div class="when">MONDAY | 26<sup>TH</sup> | 23:21</div><div class="deg">29<sup>O</sup></div>
</div>

<div class="abs more">···</div>

<!-- newsletter -->
<div class="abs newsletter" role="img" aria-label="Misty blue lake surrounded by forested hills"></div>
<div class="abs nl-title">SIGN UP TO OUR EMAIL NEWSLETTER</div>
<div class="abs nl-sub">Lorem ipsum dolor sit amet, consectetur adipisicing elit, sed do eiusmod tempor incididunt ut labore et dolore</div>
<div class="abs nl-input">Email Adress...</div>
<div class="abs nl-go">GO</div>

<!-- footer -->
<div class="abs foot-brand"><span class="dot"></span>Skyvane</div>
<div class="abs copy">© 2017 Weather Website, Inc</div>
<div class="abs links">Terms* | Privacy and Policy | Contact Us</div>
<div class="abs social"><span></span><span></span><span></span><span></span><span></span><span></span></div>

</body>
</html>
```